Design some Business Cards

I need a 2 side business card designed for my travel and entertainment business and business directory Solvane Tropica. The website url is [url removed, login to view] so you can explore the countries and see what its about. I attached the logo image and psd so you can be more creative.

Information for business card include:

Business: Solvane Tropica
Tagline: The Tropics' Foremost Enterprise Promotion Hub

Name: Bertram Halvey
Title: Founder/General Manager
Address: P.O. Box 5174
Kingstown
St. Vincent and the Grenadines

Tel: 784-517-8092
Mob: 347-582-3107
Email: bhalvey@[url removed, login to view]
Web: [url removed, login to view]

I have another business card to do also but I'm waiting on my partner logo to start another contest for that one. Thanks.

```html
<!DOCTYPE html>
<html lang="en">
<head>
<meta charset="utf-8">
<title>Solvane Tropica – Business Card</title>
<link rel="stylesheet" href="https://fonts.googleapis.com/css2?family=Montserrat:wght@400;500;700;800&display=swap">
<style>
  :root {
    --bg: #e9e6e1;
    --card: #ffffff;
    --orange: #f08a1c;
    --green: #1f9a3a;
    --ink: #2a2a2a;
    --white: #ffffff;
  }
  * { margin: 0; padding: 0; box-sizing: border-box; }
  html, body { width: 1200px; height: 900px; overflow: hidden; }
  body {
    background: var(--bg);
    font-family: "Montserrat", Arial, sans-serif;
    position: relative;
  }
  .card {
    position: absolute;
    left: 250px;
    width: 700px;
    height: 400px;
    background: var(--card);
    overflow: hidden;
    box-shadow: 0 6px 18px rgba(0,0,0,0.18);
  }
  .card--front { top: 40px; }
  .card--back { top: 470px; }
  .card svg.shape { position: absolute; inset: 0; }

  .brand {
    position: absolute;
    display: flex;
    align-items: center;
    gap: 14px;
    color: var(--green);
    font-weight: 800;
    text-transform: uppercase;
    white-space: nowrap;
  }
  .brand__dot {
    border-radius: 50%;
    background: var(--orange);
    flex: none;
  }
  .card--front .brand { left: 50%; top: 150px; transform: translateX(-50%); font-size: 54px; letter-spacing: 1px; }
  .card--front .brand__dot { width: 42px; height: 42px; }
  .front__web {
    position: absolute; right: 56px; bottom: 46px;
    color: var(--green); font-size: 20px; font-weight: 500; letter-spacing: 0.5px;
  }

  .card--back .brand { left: 200px; top: 48px; font-size: 30px; }
  .card--back .brand__dot { width: 24px; height: 24px; }
  .person {
    position: absolute; left: 272px; top: 112px;
    display: flex; flex-direction: column; align-items: flex-end;
  }
  .person__name { font-size: 26px; font-weight: 700; color: var(--ink); line-height: 1.2; }
  .person__title { font-size: 13px; font-weight: 500; color: var(--ink); margin-top: 2px; }

  .contacts {
    position: absolute; left: 40px; right: 24px; top: 238px;
    display: grid; grid-template-columns: 260px 1fr;
    grid-auto-flow: column; grid-template-rows: repeat(3, 40px);
    column-gap: 20px; row-gap: 10px;
    color: var(--white); font-size: 15px; line-height: 1.3;
  }
  .contact { display: flex; align-items: center; gap: 10px; white-space: nowrap; }
  .contact__icon {
    width: 28px; height: 28px; border: 2px solid var(--white); border-radius: 50%;
    display: flex; align-items: center; justify-content: center; flex: none;
  }
</style>
</head>
<body>

<section class="card card--front" aria-label="Card front">
  <svg class="shape" width="700" height="400" viewBox="0 0 700 400" aria-hidden="true">
    <path d="M0 0 H700 V18 C520 40 300 60 120 90 C70 98 30 110 0 125 Z" fill="var(--orange)"/>
  </svg>
  <div class="brand"><span class="brand__dot"></span>Solvane Tropica</div>
  <div class="front__web">solvanetropica.com</div>
</section>

<section class="card card--back" aria-label="Card back">
  <svg class="shape" width="700" height="400" viewBox="0 0 700 400" aria-hidden="true">
    <path d="M0 222 C220 212 470 175 700 150 V400 H0 Z" fill="var(--orange)"/>
  </svg>
  <div class="brand"><span class="brand__dot"></span>Solvane Tropica</div>
  <div class="person">
    <div class="person__name">Bertram Halvey</div>
    <div class="person__title">Founder</div>
  </div>
  <div class="contacts">
    <div class="contact">
      <span class="contact__icon"><svg width="14" height="14" viewBox="0 0 14 14"><path d="M3 1 L5 4 L4 5.5 C5 7.5 6.5 9 8.5 10 L10 9 L13 11 L11.5 13 C6 12.5 1.5 8 1 2.5 Z" fill="currentColor"/></svg></span>
      784-517-8092
    </div>
    <div class="contact">
      <span class="contact__icon"><svg width="14" height="14" viewBox="0 0 14 14"><circle cx="7" cy="7" r="5.5" fill="none" stroke="currentColor" stroke-width="1.4"/><path d="M1.5 7 H12.5 M7 1.5 C4.5 4 4.5 10 7 12.5 M7 1.5 C9.5 4 9.5 10 7 12.5" fill="none" stroke="currentColor" stroke-width="1.2"/></svg></span>
      solvanetropica.com
    </div>
    <div class="contact">
      <span class="contact__icon"><svg width="12" height="14" viewBox="0 0 12 14"><rect x="2" y="0.75" width="8" height="12.5" rx="1.5" fill="none" stroke="currentColor" stroke-width="1.5"/><circle cx="6" cy="10.5" r="1" fill="currentColor"/></svg></span>
      347-582-3107
    </div>
    <div class="contact">
      <span class="contact__icon"><svg width="14" height="10" viewBox="0 0 14 10"><rect x="0.75" y="0.75" width="12.5" height="8.5" fill="none" stroke="currentColor" stroke-width="1.5"/><path d="M1 1 L7 6 L13 1" fill="none" stroke="currentColor" stroke-width="1.5"/></svg></span>
      bhalvey@solvanetropica.com
    </div>
    <div class="contact">
      <span class="contact__icon"><svg width="14" height="14" viewBox="0 0 14 14"><path d="M7 1 L13 6 H11.5 V13 H8.5 V9 H5.5 V13 H2.5 V6 H1 Z" fill="currentColor"/></svg></span>
      <span>P.O. Box 5174 Kingstown<br>St. Vincent and the Grenadines</span>
    </div>
  </div>
</section>

</body>
</html>
```